Corvane Pharma Business Card

Corvane Pharma in the upper left hand corner with the following underneath

Validated ERP Software
Pharma | Medical Devices | Contract Manufacturing

phone (555) 418-3072 x314

fax (555) 276-9035

email jdelm@corvanesystems.example

web www.corvanesystems.example

Ashford | Bellmere | Crestvale

```html
<!DOCTYPE html>
<html lang="en">
<head>
<meta charset="utf-8">
<title>Corvane Pharma Business Card</title>
<link rel="stylesheet" href="https://fonts.googleapis.com/css2?family=Montserrat:wght@500;700;800&display=swap">
<style>
  :root {
    --brand-blue: #0b55a4;
    --brand-green: #8cc63f;
    --green-soft: #e4f1d2;
    --paper: #ffffff;
    --backdrop: #e8e9e5;
    --ink-light: #ffffff;
  }
  * { box-sizing: border-box; margin: 0; padding: 0; }
  html, body {
    width: 1200px; height: 1000px; overflow: hidden;
    background: var(--backdrop);
    font-family: "Montserrat", Arial, sans-serif;
  }
  .stage { position: relative; width: 1200px; height: 1000px; }
  .card {
    position: absolute; left: 250px; width: 700px; height: 400px;
    box-shadow: 0 10px 30px rgba(0,0,0,0.15);
    overflow: hidden;
  }
  .card--front { top: 70px; background: var(--paper); }
  .card--back { top: 530px; background: var(--brand-blue); color: var(--ink-light); }

  .corner-accent {
    position: absolute; left: 0; top: 0; width: 110px; height: 70px;
    background: linear-gradient(90deg, var(--green-soft), rgba(228,241,210,0));
  }

  .wordmark {
    position: absolute; display: flex; align-items: center; gap: 12px;
    font-weight: 800; letter-spacing: 0.5px; white-space: nowrap;
  }
  .wordmark__dot { border-radius: 50%; background: var(--brand-green); flex: none; }
  .card--front .wordmark {
    left: 50%; top: 200px; transform: translate(-50%, -50%);
    font-size: 46px; color: var(--brand-blue);
  }
  .card--front .wordmark__dot { width: 22px; height: 22px; }
  .card--back .wordmark { left: 56px; top: 62px; font-size: 36px; color: var(--ink-light); }
  .card--back .wordmark__dot { width: 18px; height: 18px; }

  .tagline {
    position: absolute; right: 48px; top: 198px; text-align: right;
    font-weight: 700; font-size: 16.5px; line-height: 27px;
  }
  .divider {
    position: absolute; left: 148px; right: 48px; top: 262px;
    height: 1.5px; background: var(--brand-green);
  }
  .contact {
    position: absolute; right: 48px; top: 276px;
    display: flex; flex-direction: column; align-items: flex-end; gap: 12px;
    font-weight: 500; font-size: 15px;
  }
  .contact__row { display: flex; gap: 22px; }
  .contact__item { display: flex; align-items: center; gap: 8px; white-space: nowrap; }
  .contact__icon { width: 18px; height: 18px; flex: none; }
</style>
</head>
<body>
<main class="stage">
  <section class="card card--front" aria-label="Card front">
    <div class="corner-accent" role="img" aria-label="Green corner accent"></div>
    <div class="wordmark"><span class="wordmark__dot"></span>Corvane Pharma</div>
  </section>

  <section class="card card--back" aria-label="Card back">
    <div class="wordmark"><span class="wordmark__dot"></span>Corvane Pharma</div>

    <p class="tagline">Validated ERP Software<br>Pharma | Medical Devices | Contract Manufacturing</p>
    <div class="divider"></div>

    <div class="contact">
      <div class="contact__row">
        <span class="contact__item">
          <svg class="contact__icon" viewBox="0 0 18 18" aria-label="email"><circle cx="9" cy="9" r="9" fill="var(--brand-green)"/><rect x="4.5" y="6" width="9" height="6.5" fill="none" stroke="var(--brand-blue)" stroke-width="1.3"/><path d="M4.5 6 L9 9.6 L13.5 6" fill="none" stroke="var(--brand-blue)" stroke-width="1.3"/></svg>
          jdelm@corvanesystems.example
        </span>
        <span class="contact__item">
          <svg class="contact__icon" viewBox="0 0 18 18" aria-label="web"><circle cx="9" cy="9" r="9" fill="var(--brand-green)"/><g fill="none" stroke="var(--brand-blue)" stroke-width="1.2"><circle cx="9" cy="9" r="4.8"/><ellipse cx="9" cy="9" rx="2" ry="4.8"/><line x1="4.2" y1="9" x2="13.8" y2="9"/></g></svg>
          www.corvanesystems.example
        </span>
      </div>
      <div class="contact__row">
        <span class="contact__item">
          <svg class="contact__icon" viewBox="0 0 18 18" aria-label="phone"><circle cx="9" cy="9" r="9" fill="var(--brand-green)"/><path d="M6 4.5 L7.8 6.6 L6.9 7.8 Q8 10.3 10.2 11.1 L11.4 10.2 L13.5 12 L12.4 13.4 Q7.6 13 4.6 6 Z" fill="var(--brand-blue)"/></svg>
          (555) 418-3072 x314
        </span>
        <span class="contact__item">
          <svg class="contact__icon" viewBox="0 0 18 18" aria-label="fax"><circle cx="9" cy="9" r="9" fill="var(--brand-green)"/><rect x="6" y="4.2" width="6" height="3.5" fill="var(--brand-blue)"/><rect x="4.2" y="7.5" width="9.6" height="5.5" rx="1" fill="var(--brand-blue)"/><rect x="6.5" y="9" width="5" height="2.5" fill="var(--brand-green)"/></svg>
          (555) 276-9035
        </span>
      </div>
      <div class="contact__row">
        <span class="contact__item">
          <svg class="contact__icon" viewBox="0 0 18 18" aria-label="locations"><circle cx="9" cy="9" r="9" fill="var(--brand-green)"/><path d="M9 14.2 Q5.2 9.6 5.2 7.6 A3.8 3.8 0 0 1 12.8 7.6 Q12.8 9.6 9 14.2 Z" fill="var(--brand-blue)"/><circle cx="9" cy="7.6" r="1.4" fill="var(--brand-green)"/></svg>
          Ashford | Bellmere | Crestvale
        </span>
      </div>
    </div>
  </section>
</main>
</body>
</html>
```